Dialogues Beyond the Quiet Horizon--Rising into Inner Clarity by Vincent L. Ostrowski. PhD

This design request is for a book cover. The book is about my higher self returning to earth as an ascended master and helicopter pilot and the ensuing conversations we have about the spiritual path. In the book there is a parable about a helicopter pilot searching for an ancient city of light as a metaphor for following our higher guidance..

The cover I have envisioned is a Corvane 52 helicopter flying in a huge, mountainous wilderness area surrounded by miles of sheer cliffs, unstable glaciers, and turbulent canyon rivers, approaching an ancient city hidden among the trees glowing in a beautiful, shimmering white light. It is magnificent. The idea here is something similar to the ancient city of Shangri-La in Tibet.

Please feel free to consider other concepts.
my website is www.authorvincentostrowski.example

FYI: A picture that captures what I am looking fir is similar to the book "The Riddle of Veloran: Seeking the Ninth Passage" by Martin Halloway.

Thank you!!

```html
<!DOCTYPE html>
<html lang="en">
<head>
<meta charset="utf-8">
<title>Dialogues Beyond the Quiet Horizon — Book Cover</title>
<link rel="stylesheet" href="https://fonts.googleapis.com/css2?family=Great+Vibes&family=Cinzel:wght@400&family=Cormorant+SC:wght@500&display=swap">
<style>
  :root {
    --page: #ffffff;
    --sky-top: #3a4a63;
    --sky-mid: #5d7383;
    --haze: #7d8a72;
    --forest: #2e4448;
    --dusk: #4a4a68;
    --ember: #b45a4a;
    --ember-deep: #7a3b44;
    --glow: rgba(255, 236, 200, 0.55);
    --ink-light: #f4f1ec;
    --rule: rgba(240, 236, 230, 0.8);
  }
  * { margin: 0; padding: 0; box-sizing: border-box; }
  html, body {
    width: 1196px;
    height: 1200px;
    overflow: hidden;
    background: var(--page);
  }
  .book-cover {
    position: absolute;
    left: 198px;
    top: 0;
    width: 800px;
    height: 1200px;
    overflow: hidden;
  }
  .cover-art {
    position: absolute;
    inset: 0;
    background:
      radial-gradient(circle at 63% 66%, var(--glow) 0, rgba(255,236,200,0) 90px),
      linear-gradient(180deg,
        var(--sky-top) 0%,
        var(--sky-mid) 16%,
        var(--dusk) 24%,
        var(--haze) 40%,
        var(--forest) 58%,
        var(--dusk) 74%,
        var(--ember-deep) 88%,
        var(--ember) 100%);
  }
  .title {
    position: absolute;
    left: 0;
    right: 0;
    top: 268px;
    text-align: center;
    font-family: "Great Vibes", cursive;
    color: var(--ink-light);
    text-shadow: 0 3px 8px rgba(0, 0, 0, 0.45);
    font-weight: 400;
  }
  .title-line { display: block; line-height: 1; }
  .title-line--lead { font-size: 74px; }
  .title-line--middle { font-size: 104px; margin-top: 6px; }
  .title-line--key { font-size: 150px; margin-top: 8px; }
  .subtitle {
    position: absolute;
    left: 180px;
    width: 440px;
    top: 872px;
    padding-bottom: 8px;
    border-bottom: 2px solid var(--rule);
    text-align: center;
    font-family: "Cormorant SC", "Cinzel", serif;
    font-size: 27px;
    letter-spacing: 2px;
    color: var(--ink-light);
  }
  .author {
    position: absolute;
    left: 0;
    right: 0;
    top: 1110px;
    text-align: center;
    font-family: "Cinzel", serif;
    font-size: 30px;
    letter-spacing: 1px;
    color: var(--ink-light);
  }
</style>
</head>
<body>
  <main class="book-cover">
    <div class="cover-art" role="img" aria-label="Painted scene: a helicopter pilot in a reflective helmet above misty mountain ranges and forest, with an ancient stone city glowing with white light among the trees"></div>
    <h1 class="title">
      <span class="title-line title-line--lead">Dialogues Beyond</span>
      <span class="title-line title-line--middle">the Quiet</span>
      <span class="title-line title-line--key">Horizon</span>
    </h1>
    <p class="subtitle">Rising into Inner Clarity</p>
    <p class="author">Vincent L. Ostrowski. PhD</p>
  </main>
</body>
</html>
```